2025 Fall Auction

Large Farm and construction online only auction November 3rd thru 5Th
Bidding Closes November 5 th at 7 pm
Now Accepting Consignment call ( 555 )-271-6038 or email Marcus@brevlandsales.com
150 + Skid Steer Attachments
50 + Pieces of farm equipment
More To Come
Consignments are welcomed Till October 25Th

Target Market(s)

New customers

```html
<!DOCTYPE html>
<html lang="en">
<head>
<meta charset="utf-8">
<title>Fall Auction Flyer</title>
<link href="https://fonts.googleapis.com/css2?family=Bebas+Neue&display=swap" rel="stylesheet">
<style>
  :root {
    --backdrop: #ececed;
    --paper: #ffffff;
    --ink: #333333;
    --orange: #f7941d;
    --grey-panel: #9b9b9b;
    --divider: #5a5a5a;
  }
  * { margin: 0; padding: 0; box-sizing: border-box; }
  html, body {
    width: 979px; height: 1200px; overflow: hidden;
    background: var(--backdrop);
    font-family: "Bebas Neue", "Oswald", sans-serif;
    color: var(--ink);
  }
  .flyer {
    position: absolute; left: 49px; top: 26px;
    width: 881px; height: 1148px;
    background: var(--paper);
    overflow: hidden;
  }
  .hero-photo {
    position: absolute; left: 0; top: 0; width: 881px; height: 345px;
    background: linear-gradient(160deg, #8c8a80 0%, #a39b86 35%, #d3a72c 55%, #b98f2a 70%, #8e8678 100%);
  }
  .torn { position: absolute; left: 0; display: block; }
  .torn-hero { top: 290px; }
  .brand-box {
    position: absolute; left: 680px; top: 0; width: 165px; height: 142px;
    background: var(--paper);
    display: flex; align-items: center; justify-content: center;
  }
  .brand-name { color: var(--ink); font-size: 28px; line-height: 1; letter-spacing: 1px; }
  .headline {
    position: absolute; left: 57px; top: 366px; width: 800px;
    font-size: 60px; line-height: 68px; font-weight: 400;
    text-align: center; white-space: nowrap;
  }
  .orange-band {
    position: absolute; left: 0; top: 600px; width: 881px; height: 400px;
    background: var(--orange);
  }
  .torn-band-top { top: 540px; }
  .torn-band-bottom { top: 985px; }
  .machine-photo {
    position: absolute; left: 30px; top: 530px; width: 340px; height: 260px;
    border-radius: 40px;
    background: radial-gradient(ellipse at 45% 45%, #e2752a 0%, #c9621f 40%, #4a3a2e 75%, #3a3a3a 100%);
  }
  .closing-panel {
    position: absolute; left: 455px; top: 525px; width: 401px; height: 228px;
    background: var(--grey-panel); color: #fff;
    font-size: 60px; line-height: 66px; text-align: center;
    padding-top: 14px;
  }
  .inventory {
    position: absolute; left: 20px; top: 832px; width: 440px;
    color: #fff; font-size: 40px; line-height: 52px; text-align: center; white-space: nowrap;
  }
  .divider {
    position: absolute; left: 467px; top: 808px; width: 1px; height: 148px;
    background: var(--divider);
  }
  .consign-contact {
    position: absolute; left: 470px; top: 818px; width: 408px;
    color: #fff; text-align: center; white-space: nowrap;
  }
  .consign-contact .lead { font-size: 29px; line-height: 34px; }
  .consign-contact .phone { font-size: 52px; line-height: 58px; margin-top: 2px; }
  .consign-contact .email { font-size: 22px; line-height: 30px; margin-top: 2px; }
  .teaser {
    position: absolute; left: 0; top: 1030px; width: 881px;
    text-align: center; font-size: 32px; line-height: 36px;
  }
  .deadline {
    position: absolute; left: 0; top: 1072px; width: 881px;
    text-align: center; font-size: 54px; line-height: 58px; white-space: nowrap;
  }
</style>
</head>
<body>
  <main class="flyer">
    <div class="hero-photo" role="img" aria-label="Photo of a yellow mini excavator parked on a gravel lot with red farm implements behind it"></div>
    <svg class="torn torn-hero" width="881" height="70" viewBox="0 0 881 70" aria-hidden="true">
      <polygon fill="#ffffff" points="0,40 20,36 38,42 60,30 82,34 100,24 125,28 150,18 170,22 190,14 215,20 240,12 262,18 288,10 310,16 335,8 360,14 385,6 410,12 432,16 455,8 480,14 505,10 530,18 552,12 575,20 600,14 625,22 648,18 672,26 695,22 720,30 745,26 770,34 795,30 820,38 845,34 865,40 881,38 881,70 0,70"/>
    </svg>
    <div class="brand-box">
      <span class="brand-name">BREVLAND SALES</span>
    </div>

    <h1 class="headline">LARGE FARM AND CONSTRUCTION ONLINE<br>ONLY AUCTION NOVEMBER 3RD THRU 5TH</h1>

    <svg class="torn torn-band-top" width="881" height="64" viewBox="0 0 881 64" aria-hidden="true">
      <polygon fill="#f7941d" points="0,62 15,50 30,44 48,40 60,32 78,30 95,36 110,30 130,34 150,28 170,34 190,30 210,36 232,32 250,38 270,34 290,40 310,36 330,42 350,38 370,44 390,40 410,46 430,42 455,44 455,64 0,64"/>
      <polygon fill="#f7941d" points="845,40 860,34 872,38 881,36 881,64 845,64"/>
    </svg>
    <div class="orange-band"></div>
    <svg class="torn torn-band-bottom" width="881" height="40" viewBox="0 0 881 40" aria-hidden="true">
      <polygon fill="#ffffff" points="0,10 18,16 35,8 55,14 75,10 95,18 118,12 140,16 162,10 185,18 205,14 228,20 250,12 272,16 295,10 318,18 340,14 362,20 385,12 408,16 430,8 452,14 475,10 498,18 520,12 542,16 565,8 588,14 610,10 632,18 655,12 678,16 700,10 722,18 745,14 768,20 790,12 812,18 835,14 858,20 881,16 881,40 0,40"/>
    </svg>

    <div class="machine-photo" role="img" aria-label="Photo of an orange compact tracked skid steer with a black bucket"></div>

    <div class="closing-panel">BIDDING CLOSES<br>NOVEMBER<br>5 TH AT 7 PM</div>

    <div class="inventory">150 + SKID STEER ATTACHMENTS<br>50 + PIECES OF FARM EQUIPMENT</div>
    <div class="divider"></div>
    <div class="consign-contact">
      <p class="lead">NOW ACCEPTING CONSIGNMENT</p>
      <p class="phone">CALL ( 555 )-271-6038</p>
      <p class="email">OR EMAIL MARCUS@BREVLANDSALES.COM</p>
    </div>

    <p class="teaser">MORE TO COME</p>
    <p class="deadline">CONSIGNMENTS ARE WELCOMED TILL OCTOBER 25TH</p>
  </main>
</body>
</html>
```